Create Bourbon label for Craft Distillery located in the Foothills of NC.

Need to create a label for a craft bourbon. The brand name is Creekhollow. Looking for a traditional/vintage bottle label. I have created a concept and would like an expansion of the concept idea (open to artwork outside of concept art as well). I have included the bottle being used. Label area approx 4.25H x 3.5W. With the Creekhollow brand name, would like to incorporate trees (native to NC and Appalachia), mountains (mt pano of area included), and sawblade. However, I do not want the sawblade to be the focal point of the design. The word Bourbon, proof, abv, and 750 ml will need to be horizontal. Creekhollow and Made in NC can be angled in the design.

Requirements
Must have
• Front Label will need to contain the followingBrand Name = SawmillsBourbon750 ml100 Proof50% ABVAged 3 years

```html
<!DOCTYPE html>
<html lang="en">
<head>
<meta charset="utf-8">
<title>Creekhollow Bourbon Label</title>
<link rel="stylesheet" href="https://fonts.googleapis.com/css2?family=Archivo+Black&family=Arimo:wght@400;700&display=swap">
<style>
  :root {
    --paper: #ffffff;
    --ink: #111111;
    --forest-deep: #2c3a22;
    --forest-mid: #4f6b33;
    --bark: #5a3322;
    --floor: #6e6a4c;
  }
  html, body {
    margin: 0;
    padding: 0;
    width: 992px;
    height: 1200px;
    overflow: hidden;
    background: var(--paper);
  }
  .label {
    display: block;
    width: 992px;
    height: 1200px;
  }
  .brand-name {
    font-family: "Archivo Black", "Arial Black", sans-serif;
    fill: var(--paper);
  }
  .product-type {
    font-family: "Archivo Black", "Arial Black", sans-serif;
    fill: var(--ink);
    letter-spacing: 14px;
  }
  .spec {
    font-family: "Arimo", Arial, sans-serif;
    fill: var(--paper);
  }
  .spec--bold { font-weight: 700; }
  .band, .blade { fill: var(--paper); }
</style>
</head>
<body>
<svg class="label" viewBox="0 0 992 1200" xmlns="http://www.w3.org/2000/svg">
  <defs>
    <linearGradient id="forestTone" x1="0" y1="0" x2="0" y2="1">
      <stop offset="0" stop-color="var(--forest-mid)"/>
      <stop offset="0.35" stop-color="var(--forest-deep)"/>
      <stop offset="0.7" stop-color="var(--bark)"/>
      <stop offset="1" stop-color="var(--floor)"/>
    </linearGradient>
    <radialGradient id="treeTone" cx="0.5" cy="0.6" r="0.6">
      <stop offset="0" stop-color="#ffffff" stop-opacity="0.9"/>
      <stop offset="1" stop-color="#ffffff" stop-opacity="0.15"/>
    </radialGradient>
    <clipPath id="labelArea">
      <rect x="24" y="24" width="944" height="1152"/>
    </clipPath>
    <clipPath id="belowBand">
      <rect x="-200" y="739" width="1400" height="700"/>
    </clipPath>
  </defs>

  <rect class="forest-scene" x="24" y="24" width="944" height="1152" fill="url(#forestTone)" role="img" aria-label="Photograph of a tall pine forest with reddish trunks and a grassy floor"/>

  <polygon class="tree-cluster" points="198,520 260,315 330,290 400,270 480,95 560,200 640,205 700,200 784,400 784,432 198,528" fill="url(#treeTone)" role="img" aria-label="Silhouette of a row of white pine trees"/>

  <g class="emblem" clip-path="url(#labelArea)">
    <g transform="rotate(-9.2 496 610)">
      <rect class="band band--upper" x="-200" y="471" width="1400" height="20"/>
      <rect class="band band--lower" x="-200" y="719" width="1400" height="20"/>
      <text class="brand-name" x="496" y="684" font-size="205" text-anchor="middle" textLength="900" lengthAdjust="spacingAndGlyphs">CREEKHOLLOW</text>
      <circle class="blade" cx="500" cy="722" r="245" clip-path="url(#belowBand)"/>
    </g>
  </g>

  <text class="product-type" x="516" y="890" font-size="34" text-anchor="middle">BOURBON</text>

  <text class="spec spec--bold" x="74" y="1128" font-size="22">100 Proof</text>
  <text class="spec" x="496" y="1128" font-size="40" text-anchor="middle">750 ML</text>
  <text class="spec spec--bold" x="939" y="1128" font-size="22" text-anchor="end">50%ABV</text>
</svg>
</body>
</html>
```